Bluetooth Earphone Packaging Design

We want to use the packaging for 4-5 of our Bluetooth Earphone series (Picture enclosed) and hence we would not like to put any product pictures on the packaging.

Material: E-Flute Paper box
Type: Window Box style
Design features we prefer: Colorful, creative, trendy, High tech.
Requirement: AI file is preferred
Size of Packaging: (L) 95 x (W) 40 x (H) 120 mm

Enclosed are a detailed description along with competitor designs for your reference.

Any further questions, please feel free to ask

```html
<!DOCTYPE html>
<html lang="en">
<head>
<meta charset="utf-8">
<title>Bluetooth Earphone 5.0 – Packaging</title>
<link rel="stylesheet" href="https://fonts.googleapis.com/css2?family=Exo+2:wght@500;600;700&display=swap">
<style>
  :root {
    --bg: #d9d9db;
    --teal-top: #1c90ad;
    --teal-bottom: #0d6f8c;
    --spine: #1f1f20;
    --band: #333234;
    --window-top: #707072;
    --window-bottom: #58585a;
    --ink: #ffffff;
    --rule: rgba(255,255,255,0.75);
  }
  * { margin: 0; padding: 0; box-sizing: border-box; }
  html, body { width: 1200px; height: 1200px; overflow: hidden; }
  body {
    background: var(--bg);
    font-family: "Exo 2", "Arial", sans-serif;
    color: var(--ink);
    position: relative;
  }
  .spine {
    position: absolute;
    left: 195px; top: 240px;
    width: 240px; height: 720px;
    background: var(--spine);
    display: flex; align-items: center; justify-content: center;
  }
  .spine-title {
    writing-mode: vertical-rl;
    font-size: 44px;
    font-weight: 600;
    letter-spacing: 2px;
    white-space: nowrap;
  }
  .front {
    position: absolute;
    left: 435px; top: 240px;
    width: 570px; height: 720px;
    background: linear-gradient(180deg, var(--teal-top), var(--teal-bottom));
    overflow: hidden;
  }
  .product-title {
    position: absolute;
    right: 60px; top: 48px;
    font-size: 34px; font-weight: 600;
    line-height: 1.12;
    text-align: right;
    letter-spacing: 1px;
  }
  .version-band {
    position: absolute;
    left: 300px; right: 0; top: 148px;
    height: 76px;
    background: var(--band);
    display: flex; align-items: center; justify-content: flex-end;
    padding-right: 60px;
  }
  .version-number {
    font-size: 64px; font-weight: 700;
    letter-spacing: 3px;
    line-height: 1;
  }
  .brand-mark {
    position: absolute;
    right: 60px; top: 250px;
    display: flex; align-items: center; gap: 7px;
    font-size: 20px; font-weight: 600;
  }
  .brand-dot {
    width: 12px; height: 12px; border-radius: 50%;
    background: var(--ink);
  }
  .window {
    position: absolute;
    left: 60px; top: 300px;
    width: 280px; height: 380px;
    border-radius: 24px;
    background: linear-gradient(180deg, var(--window-top), var(--window-bottom));
  }
  .feature-list {
    position: absolute;
    right: 60px; top: 390px;
    list-style: none;
    text-align: right;
    font-size: 24px; font-weight: 600;
    line-height: 1.15;
    letter-spacing: 0.5px;
  }
  .feature-list li { padding: 14px 0; }
  .feature-list li + li::before {
    content: "";
    display: block;
    width: 90px; height: 1.5px;
    background: var(--rule);
    margin: 0 0 18px auto;
    position: relative; top: -14px;
  }
</style>
</head>
<body>
  <section class="spine">
    <span class="spine-title">Bluetooth Earphone 5.0</span>
  </section>

  <section class="front">
    <h1 class="product-title">Bluetooth<br>Earphone</h1>
    <div class="version-band"><span class="version-number">5.0</span></div>
    <div class="brand-mark"><span class="brand-dot"></span><span>Linkwave</span></div>
    <div class="window" role="img" aria-label="Die-cut window showing the earphones inside"></div>
    <ul class="feature-list">
      <li>Bluetooth 5.0</li>
      <li>Exceptional<br>Sound Quality</li>
      <li>High Definition<br>Microphone</li>
    </ul>
  </section>
</body>
</html>
```